Web Design Project

Website Design Brief

Company Details
1a) Name of Company

FERNHOLLOW
1) What is the nature of your business?: Briefly describe your products or services:

INDEPENDENT CONTEMPORARY TRADITIONAL ITALIAN RESTAURANT IN THE HEART OF ST BARNABYS QUAY ALSO CATERING FOR PRIVATE CORPORATE EVENTS AND WEDDING RECEPTIONS

1a) Who is your target market? Who are you hoping to reach with your site?

CITY CORPORATES, LOCAL CORPORATES/BUSINESSES, LOCAL RESIDENTS, VISITORS TO THE DOCK, LOCAL HOTELS

Website Details
1b) Do you have an existing website? If so, what is the URL?
HTTP://WWW.FERNHOLLOWTRATTORIA.EXAMPLE

2b) IMPORTANT: Please list at least 3 URLs (web addresses) of high quality sites that you like the look of (these do not have to be sites who’s business is similar to yours. It aids us in determining what your design style is.) Please consider layout, colours, navigation, graphics, and typography.

http://www.thecorvell.example/

http://www.mordasque.example/

http://www.tivokitchen.example/

http://www.perzola.example/

3b) What colours or colour schemes would you like?

WHITE, BLACK, SILVER/ALUMINIUM (PLS LOOK AT OUR OUTSIDE CHAIRS)

4b) List the Navigation links for your Site:

5b) What type of look are you trying to achieve? (e.g. clean, high-tech, conservative, warm, flashy, etc.)

SIMPLE ELEGANT CLASSY INFORMATIVE, EASY TO USE, A REFLECTION OF THE BUSINESS ITSELF

6b) Please provide the addresses of competitors' sites, if possible:

Do not contact the client direct - all questions should go through Wendmoor Catering - info@wendmoorcatering.example
Updates

thanks for the designs that I have received so far. I have these general comments:

- please avoid using icons for phones or paperclips etc 
- use dummy text (one design used text from another website) 
- there won't any live social media feeds to the site
the client likes a lot of the designs that this company comes up with: 

i look forward to see some more designs

hi all, 

further to my last update, here are a few more pointers:
- there will be no search facilities - so no "search" box please 
- please just use the images supplied - no stock ones
- use just the page names give (no other pages) 

The client is looking for a simple, elegant design. 

Many thanks 
Neil 

thanks for all the designs. 

I have uploaded another file to the brief which shows some posters that the client particularly likes. Perhaps the homepage could consist of large rectangle made up of a number of boxes - for some introductory text, a large image, mailing list, contact details, Lunch Special etc - just an idea! 
It's clear that the client likes clean lines with square edges. 
I want to be able to pass the designs directly onto the client so can designers avoid adding extra info or page. For example one design has a tab for a "Gift Card" - it will be easier for me if such additions are avoided. 

thanks!                                                                                                                                                                                                                                                                                                                                                                                                    

Thank you for all your designs - please keep them coming! 

hi all,

I am meeting the client tomorrow afternoon so please submit revisions / designs before then. 

Many thanks, 
Neil

Target Market(s)

Business people, upmarket etc

Industry/Entity Type

Business

Requirements
Must have
• - The home page needs a slide show of images as well as:
- a mailing list form - very simple, "Join our mailing list - name, email"
- 3 or 4 sentences of text
- Friendsheet link

```html
<!DOCTYPE html>
<html lang="en">
<head>
<meta charset="utf-8">
<title>Fernhollow Italian</title>
<link href="https://fonts.googleapis.com/css2?family=Raleway:wght@300;400;600&family=Arimo:wght@400;700&family=Oswald:wght@400;500&family=Fondamento&family=Arvo:wght@700&family=Parisienne&display=swap" rel="stylesheet">
<style>
:root{
  --page:#e3e5e8;
  --white:#ffffff;
  --ink:#1d1d1d;
  --text:#4a4a4a;
  --muted:#9a9a9a;
  --accent:#d9341c;
  --teal:#1f6f78;
  --panel:#e6fbfc;
  --footer:#23272e;
  --gold:#f2c630;
  --mint:#8fd3ad;
}
*{margin:0;padding:0;box-sizing:border-box}
html,body{width:1008px;height:1200px;overflow:hidden}
body{background:var(--page);font-family:"Arimo",Arial,sans-serif;color:var(--text);position:relative}
.abs{position:absolute}

.topbar .phone{left:704px;top:12px;font:400 18px "Raleway",sans-serif;color:var(--ink)}
.topbar .phone b{font-weight:400;color:#333}
.header{left:0;top:42px;width:1008px;height:46px;background:var(--white)}
.brand{left:114px;top:47px;font:400 30px "Raleway",sans-serif;color:var(--ink);letter-spacing:1px}
.brand small{display:block;font-size:11px;letter-spacing:5px;margin-left:60px;margin-top:-2px}
.nav{left:370px;top:59px;display:flex;gap:26px;font:400 12px "Raleway",sans-serif;color:var(--ink);list-style:none}
.nav li.active{color:#666;border-bottom:4px solid #444;padding-bottom:10px}

.slider{left:92px;top:107px;width:824px;height:376px;background:#f3f4f5;box-shadow:0 4px 8px rgba(0,0,0,.15)}
.slide-img{left:101px;top:115px;width:806px;height:358px;background:radial-gradient(circle at 40% 45%,#c9d27a 0,#6f8a3a 22%,#caa362 45%,#8a6a3a 65%,#3d3a33 100%)}
.caption{left:92px;top:224px;width:374px;height:154px;background:rgba(70,70,70,.72);padding:8px 20px}
.caption h2{font:400 46px "Fondamento",cursive;color:var(--white);line-height:54px}
.caption hr{border:0;border-top:4px dotted var(--white);margin:4px 0 6px;width:340px}
.caption p{font:300 23px/34px "Raleway",sans-serif;color:var(--white)}
.ribbon{left:807px;top:115px}
.dots{left:107px;top:452px;display:flex;gap:3px;background:rgba(0,0,0,.4);padding:4px}
.dots span{width:6px;height:6px;background:var(--white)}
.dots span:first-child{background:#111}

.card{top:493px;width:265px;height:166px;background:linear-gradient(#fff,#ececec);border:1px solid #cfd1d4;border-radius:6px;padding:8px 11px}
.card h3{font:400 13px "Raleway",sans-serif;color:var(--ink);margin-bottom:5px}
.card .thumb{height:64px;border:1px solid #ccc}
.card p{font-size:10px;line-height:15px;margin-top:7px;color:#333}

.intro{left:101px;top:676px;width:520px}
.intro h1{font:400 24px "Oswald",sans-serif;color:var(--ink);letter-spacing:-.3px}
.intro h4{font:400 13px "Arimo",sans-serif;color:var(--accent);margin:2px 0 14px}
.intro p{font-size:10.5px;line-height:15px;margin-bottom:15px;color:#555}
.video-title{left:665px;top:673px;font:400 24px "Oswald",sans-serif;color:var(--ink)}
.video{left:662px;top:707px;width:251px;height:162px;border:1px solid #bbb;background:linear-gradient(#f0f0f0,#8a8670 40%,#5e6b73 70%,#dfe3e6)}

.panel{left:92px;top:880px;width:824px;height:279px;background:var(--panel);border:1px solid #c7d3d4}
.envelope{left:114px;top:901px;width:401px;height:156px;background:linear-gradient(135deg,#1f6f78,#8bbf3f)}
.envelope-inner{left:126px;top:916px;width:376px;height:130px;background:var(--white)}
.news-title{left:188px;top:924px;font:500 21px "Oswald",sans-serif;color:var(--teal)}
.field{top:963px;width:174px;height:32px;border:1.5px solid var(--teal);border-radius:4px;font-size:11px;color:#888;padding:9px 11px;background:var(--white)}
.submit{left:139px;top:1008px;width:105px;height:24px;border-radius:12px;background:linear-gradient(#9fb9cc,#6d8ea8);color:var(--white);font:400 13px "Oswald",sans-serif;text-align:center;line-height:24px}
.social-title{left:101px;top:1070px;font:400 24px "Parisienne",cursive;color:var(--ink)}
.social{top:1107px;width:168px;height:40px;border-radius:3px;display:flex;align-items:center;color:var(--white)}
.social .label{width:58px;font:600 9px/10px "Raleway",sans-serif;padding-left:11px;letter-spacing:.5px}
.social .name{flex:1;font:600 17px "Raleway",sans-serif;text-align:center}
.social.chirp{left:120px;background:#3d9bb8}
.social.chirp .label{background:#2c7d97;height:100%;padding-top:10px}
.social.friends{left:302px;background:#3b4f8c}
.social.friends .label{background:#2e3e70;height:100%;padding-top:10px}

.dish-img{left:527px;width:126px;height:95px}
.dish{left:665px}
.dish h3{font:700 22px "Arvo",serif;color:var(--ink);letter-spacing:.5px}
.dish .place{font-size:11px;color:#888;margin-top:1px}
.dish .place span{color:var(--accent)}
.badges{display:flex;gap:6px;margin-top:7px}
.badge{height:21px;border-radius:3px;font:700 15px/21px "Arimo",sans-serif;color:var(--white);padding:0 5px}
.badge.rate{background:var(--gold);width:46px}
.badge.price{background:var(--mint);width:50px;text-align:center}
.dish .rev{font-size:7px;color:#aaa;margin-top:4px}
.dish .view{display:inline-block;font-size:7px;color:#777;border:1px solid #bbb;border-radius:2px;padding:1px 8px;margin-top:3px;background:#fff}
.divider{left:527px;top:1025px;width:389px;height:1px;background:#cde3e5}

.footer{left:0;top:1161px;width:1008px;height:28px;background:var(--footer);color:var(--white);font-size:10.5px}
.footer ul{position:absolute;left:108px;top:8px;display:flex;gap:12px;list-style:none}
.footer .address{position:absolute;left:517px;top:8px}
</style>
</head>
<body>
<div class="topbar"><div class="abs phone">Telephone: <b>0207946 0132</b></div></div>
<div class="abs header"></div>
<div class="abs brand">FERNHOLLOW<small>ITALIAN</small></div>
<ul class="abs nav">
  <li class="active">Welcome</li><li>Our Restaurant</li><li>Our Menu</li><li>Gallery</li><li>Events</li><li>Reservations</li><li>Contants</li>
</ul>

<div class="abs slider"></div>
<div class="abs slide-img" role="img" aria-label="Close-up photo of a plated Italian dish with grilled fish, salad leaves and raspberries"></div>
<div class="abs caption">
  <h2>Free Venue Hire!</h2>
  <hr>
  <p>Book Your Next Event at The Fernhollow Italian</p>
</div>
<svg class="abs ribbon" width="100" height="100" viewBox="0 0 100 100">
  <polygon points="0,0 30,0 100,70 100,100" fill="#2a2a2a"/>
  <text x="55" y="42" fill="#fff" font-family="Raleway, sans-serif" font-size="13" font-weight="600" transform="rotate(45 55 42)" text-anchor="middle">FEATURED</text>
</svg>
<div class="abs dots"><span></span><span></span><span></span><span></span></div>

<div class="abs card" style="left:94px">
  <h3>The Finest Italian Foods</h3>
  <div class="thumb" role="img" aria-label="Photo of pasta with tomato sauce and basil" style="background:linear-gradient(90deg,#fafafa,#e8d3a8 45%,#c5432a 70%,#f5f5f5)"></div>
  <p>Fernhollow incorporates the finest Italian Modern cuisine and personalized wine list supplied directly from vineyards across the globe.</p>
</div>
<div class="abs card" style="left:373px">
  <h3>Wine and Dine</h3>
  <div class="thumb" role="img" aria-label="Photo of wine bottles and vine leaves" style="background:linear-gradient(90deg,#d8e0b8,#6e8d2e 30%,#8a1b1b 45%,#c9d7a4 70%,#f0f3e6)"></div>
  <p>Our unique wine list has been personally hand picked by the owner who has a passion for fine wine and cuisine..</p>
</div>
<div class="abs card" style="left:652px">
  <h3>Events and Private Hire</h3>
  <div class="thumb" role="img" aria-label="Photo of a reserved sign on a dining table" style="background:linear-gradient(90deg,#2a1a12,#7a4a2e 35%,#d8cdb6 60%,#eee)"></div>
  <p>Fernhollow is a unique, elegant venue situated on the first floor of the historic St Barnabys Quay yacht club.</p>
</div>

<section class="abs intro">
  <h1>You Will Love Every bit of Our Traditional Cuisine</h1>
  <h4>What a year for good food and wine!</h4>
  <p>Fernhollow Italian is a stunning contemporary restaurant located in the heart of the luxurious St Barnabys Quay. The ourside terraces overlooking St Barnabys Quay Provide a truly magical experience at any time of the year.</p>
  <p>Fernhollow Italian incorporates Italy's new age cuisine and with our chefs orignating from sardinia, Turin and Naples, They have never failed to deliver inspiration and flair to the menu.</p>
  <p>We also pride ourselves with our personalised wine list supplied directly from vineyards across the globe.</p>
</section>
<div class="abs video-title">Featured Video</div>
<div class="abs video" role="img" aria-label="Video still of the restaurant terrace overlooking the quay"></div>
<svg class="abs" style="left:765px;top:765px" width="46" height="46" viewBox="0 0 46 46">
  <circle cx="23" cy="23" r="21" fill="#f4a21c" stroke="#fff" stroke-width="2"/>
  <polygon points="17,12 34,23 17,34" fill="#fff"/>
</svg>

<div class="abs panel"></div>
<div class="abs envelope" role="img" aria-label="Airmail envelope border in teal and green"></div>
<div class="abs envelope-inner"></div>
<div class="abs news-title">Newsletter</div>
<div class="abs field" style="left:134px">Name:</div>
<div class="abs field" style="left:315px">Email:</div>
<div class="abs submit">Submit</div>
<div class="abs social-title">Social Media</div>
<div class="abs social chirp"><div class="label">FOLLOW<br>US ON</div><div class="name">Chirpline</div></div>
<div class="abs social friends"><div class="label">LIKE<br>US ON</div><div class="name">Friendsheet</div></div>

<div class="abs dish-img" style="top:904px;background:linear-gradient(135deg,#c9a45a,#8a7a3a 50%,#4a3a22)" role="img" aria-label="Photo of a pizza"></div>
<div class="abs dish" style="top:905px">
  <h3>Pizza Alta</h3>
  <div class="place"><span>Harbor Oven Brewhouse</span>, Cresta Point</div>
  <div class="badges"><div class="badge rate">4.3★</div><div class="badge price">$15</div></div>
  <div class="rev">reviewed by 3 people</div>
  <div class="view">view dish</div>
</div>
<div class="abs divider"></div>
<div class="abs dish-img" style="top:1038px;background:linear-gradient(135deg,#d9d2c4,#9a5a32 45%,#5a3a24 70%,#cfc6b4)" role="img" aria-label="Photo of a loaded wrap on a plate"></div>
<div class="abs dish" style="top:1039px">
  <h3>Ember Wrap</h3>
  <div class="place"><span>Casa Verano Cafe</span>, Bayline</div>
  <div class="badges"><div class="badge rate">4.3★</div><div class="badge price">$55</div></div>
  <div class="rev">reviewed by 9 people</div>
  <div class="view">view dish</div>
</div>

<footer class="abs footer">
  <ul><li>Welcome</li><li>Our Restaurant</li><li>Our Menu</li><li>Gallery</li><li>Events</li><li>Reservations</li><li>Contants</li></ul>
  <div class="address">The Fernhollow Italian | 12 Barnaby Quay Walk, City of London, E9Q2ZZ,</div>
</footer>
</body>
</html>
```